Postcard Design

I am promoting a local school tax levy increase. I need a post card that helps market this. I saw a nice one online that someone did and I'd like something similar. I am attaching a picture of it.
Our election is April 7, 2015 and we want people to vote YES on it!
My bullet points will be: Our Children Our District Our Future
Our colors are Kelly Green and Canary but it is not mandatory that the postcards be those colors. I really like the image I sent you.
We also need to have the name of the ballot measure in smaller print under the date on the side which is: "Proposition Cedar Hollow East High School"
We also need it to say: "Advertisement paid for by the Cedar Hollow East High School Election Committee, Marla Keefe Treasurer.
For the back, you can put our name, address, and a picture of our proposed school which is image #2. You can also put: Call Doug Halvorsen @ 417-555-0187 for more information or to register for an upcoming Q&A forum.
Our name/Address is: Cedar Hollow East High School Election Committee
2756 County Road 3315
Larkdale, MO 65712
You can also include the chatterbook symbol on our card as we are on chatterbook and can include our web address as well which is: www.cedarholloweasthigh.com

Please spell check everything!

Please send me your ideas. I will need postage and address which I will provide once the proof is approved.
Thanks, Doug Halvorsen 417-555-0187

```html
<!DOCTYPE html>
<html lang="en">
<head>
<meta charset="utf-8">
<title>Cedar Hollow East High School – Vote Yes Postcard</title>
<link rel="stylesheet" href="https://fonts.googleapis.com/css2?family=Exo+2:wght@400;500;600;700;800;900&family=Open+Sans:wght@400;600;700&display=swap">
<style>
  :root {
    --canary: #fcee21;
    --ink: #111111;
    --slate: #6b6b6b;
    --rule: #9a9a9a;
    --paper: #ffffff;
    --backdrop: #e4e4e4;
    --edge: #8c8a6a;
    --building-top: #7d7d7d;
    --building-bottom: #4a4a4a;
    --photo-sky: #dfe6ea;
    --photo-ground: #8fa06e;
  }
  * { box-sizing: border-box; margin: 0; padding: 0; }
  html, body { width: 900px; height: 1200px; overflow: hidden; }
  body {
    background: var(--backdrop);
    position: relative;
    font-family: "Exo 2", sans-serif;
    color: var(--ink);
  }

  /* ---------- Front ---------- */
  .card-front {
    position: absolute; left: 80px; top: 36px;
    width: 744px; height: 574px;
    background: var(--canary);
  }
  .slogan {
    position: absolute; left: 0; right: 0; top: 30px;
    text-align: center;
    font-weight: 700; font-size: 29px; letter-spacing: 0.5px;
  }
  .rule-top {
    position: absolute; left: 19px; width: 705px; top: 79px;
    border-top: 2px solid var(--ink);
  }
  .election-date {
    position: absolute; left: 54px; top: 150px;
    font-weight: 900; font-size: 98px; line-height: 84px;
    letter-spacing: -3px;
  }
  .vote-mark {
    position: absolute; left: 340px; top: 108px;
    width: 260px; height: 250px;
  }
  .vote-word {
    position: absolute; left: 504px; top: 212px;
    font-weight: 400; font-size: 112px; line-height: 1;
    letter-spacing: -2px;
  }
  .yes-word {
    position: absolute; left: 360px; top: 336px;
    font-weight: 900; font-size: 194px; line-height: 1;
    letter-spacing: -6px;
    text-shadow:
      1.5px 0 0 var(--edge), -1.5px 0 0 var(--edge),
      0 1.5px 0 var(--edge), 0 -1.5px 0 var(--edge);
  }
  .measure-label {
    position: absolute; left: 70px; top: 436px;
    font-family: "Open Sans", sans-serif;
    font-size: 13px; color: var(--slate);
  }
  .building-art {
    position: absolute; left: 53px; top: 455px;
    width: 246px; height: 43px;
    background: linear-gradient(var(--building-top), var(--building-bottom));
  }
  .measure-name {
    position: absolute; left: 70px; top: 498px;
    font-family: "Open Sans", sans-serif;
    font-size: 14px; color: var(--slate); letter-spacing: 0.2px;
  }
  .rule-bottom {
    position: absolute; left: 19px; width: 705px; top: 533px;
    border-top: 1px solid #b8ad2a;
  }
  .disclaimer {
    position: absolute; right: 22px; top: 540px;
    font-family: "Open Sans", sans-serif;
    font-size: 9px; color: #444;
  }

  /* ---------- Back ---------- */
  .card-back {
    position: absolute; left: 80px; top: 630px;
    width: 598px; height: 458px;
    background: var(--paper);
    font-family: "Exo 2", sans-serif;
  }
  .committee-name {
    position: absolute; left: 23px; top: 26px;
    font-weight: 500; font-size: 14.5px;
  }
  .committee-address {
    position: absolute; left: 35px; top: 43px;
    font-size: 12.5px; color: #444;
  }
  .back-rule {
    position: absolute; left: 0; top: 64px; width: 448px;
    border-top: 2px solid var(--ink);
  }
  .call-label {
    position: absolute; left: 14px; top: 80px;
    font-size: 10px; color: #333;
  }
  .contact-line {
    position: absolute; left: 14px; top: 94px;
    font-weight: 600; font-size: 13px;
  }
  .contact-note {
    position: absolute; left: 14px; top: 113px;
    font-size: 9px; color: #333; letter-spacing: 0.2px;
  }
  .stamp-zone {
    position: absolute; left: 462px; top: 23px;
    width: 109px; height: 109px;
  }
  .mini-date {
    position: absolute; left: 30px; top: 162px;
    font-weight: 900; font-size: 24px; line-height: 21px;
    letter-spacing: -1px;
  }
  .mini-mark {
    position: absolute; left: 102px; top: 140px;
    width: 70px; height: 68px;
  }
  .mini-vote {
    position: absolute; left: 147px; top: 170px;
    font-size: 29px; line-height: 1; letter-spacing: -1px;
  }
  .mini-yes {
    position: absolute; left: 106px; top: 203px;
    font-weight: 900; font-size: 50px; line-height: 1; letter-spacing: -2px;
  }
  .address-lines {
    position: absolute; left: 319px; top: 209px; width: 252px;
  }
  .address-lines span {
    display: block; height: 35px;
    border-top: 1px solid var(--rule);
  }
  .web-address {
    position: absolute; left: 28px; top: 267px;
    font-weight: 700; font-size: 13.5px;
  }
  .social-line {
    position: absolute; left: 34px; top: 286px;
    font-size: 11px;
  }
  .social-line strong { font-weight: 700; font-size: 13px; }
  .school-photo {
    position: absolute; left: 0; top: 308px;
    width: 286px; height: 68px;
    background: linear-gradient(var(--photo-sky) 0%, #c9ccc8 55%, #9aa08c 80%, var(--photo-ground) 100%);
  }
  .photo-rule {
    position: absolute; left: 0; top: 376px; width: 304px;
    border-top: 2px solid var(--ink);
  }
</style>
</head>
<body>

<section class="card-front">
  <h1 class="slogan">OUR CHILDREN - OUR DISTRICT - OUR FUTURE</h1>
  <div class="rule-top"></div>

  <div class="election-date">APR7<br>2015</div>

  <svg class="vote-mark" viewBox="0 0 260 250" aria-hidden="true">
    <rect x="8" y="32" width="182" height="208" fill="none" stroke="#111" stroke-width="3"/>
    <rect x="14" y="38" width="170" height="196" fill="none" stroke="#8c8a6a" stroke-width="1.5"/>
    <polygon points="32,130 72,108 100,170 222,6 252,18 104,222"
             fill="#111" stroke="#8c8a6a" stroke-width="2" stroke-linejoin="round"/>
  </svg>
  <div class="vote-word">OTE</div>
  <div class="yes-word">YES</div>

  <div class="measure-label">PROPOSITION</div>
  <div class="building-art" role="img" aria-label="Drawing of the proposed Cedar Hollow East High School building"></div>
  <div class="measure-name">CEDAR HOLLOW EAST HIGH SCHOOL</div>

  <div class="rule-bottom"></div>
  <p class="disclaimer">Advertisement paid for by the Cedar Hollow East High School Election Committee, Marla Keefe Treasurer</p>
</section>

<section class="card-back">
  <h2 class="committee-name">CEDAR HOLLOW EAST HIGH SCHOOL ELECTION COMMITTEE</h2>
  <p class="committee-address">2756 County Road 3315 - Larkdale, MO 65712</p>
  <div class="back-rule"></div>

  <p class="call-label">CALL</p>
  <p class="contact-line">DOUG HALVORSEN @ 417-555-0187</p>
  <p class="contact-note">FOR MORE INFORMATION OR TO REGISTER FOR AN UPCOMING Q&amp;A FORUM.</p>

  <svg class="stamp-zone" viewBox="0 0 109 109" aria-hidden="true">
    <g fill="none" stroke="#9a9a9a" stroke-width="1.2">
      <path d="M1,22 V1 H22"/>
      <path d="M87,1 H108 V22"/>
      <path d="M1,87 V108 H22"/>
      <path d="M87,108 H108 V87"/>
    </g>
  </svg>

  <div class="mini-date">APR7<br>2015</div>
  <svg class="mini-mark" viewBox="0 0 260 250" aria-hidden="true">
    <rect x="8" y="32" width="182" height="208" fill="none" stroke="#111" stroke-width="8"/>
    <polygon points="32,130 72,108 100,170 222,6 252,18 104,222" fill="#111"/>
  </svg>
  <div class="mini-vote">OTE</div>
  <div class="mini-yes">YES</div>

  <div class="address-lines"><span></span><span></span><span></span><span></span></div>

  <p class="web-address">www.cedarholloweasthigh.com</p>
  <p class="social-line">and also on <strong>chatterbook</strong></p>

  <div class="school-photo" role="img" aria-label="Photo of the proposed Cedar Hollow East High School"></div>
  <div class="photo-rule"></div>
</section>

</body>
</html>
```